Modern business card for triathlon training business in Australia

We need a business card design for our triathlon training company.

Pace with Us Fitness is an Australian business, owned by women, run for women. Pace with Us Fitness helps women prepare or improve triathlon skills and confidence through triathlon camps completely designed for women.

Our camps focus on preparing women both physically and mentally for their next (or first!) triathlon.

You can see our website www.pacewithusfitness.com.au for more info about our business and our style.

We've attached two of our logos and are happy to consider a design that utilised either colour scheme with the teal colour being our 'feature' colour. We don't want overly feminine cards but rather cards that are professional and neat. If the inclusion of any pictures/art is warranted, this should be focused on our swim/ride/run theme and in that specific order (swim/ride/run).

The business card needs to be a printable design and the contact details will need to change for our two employees.

Target Market(s)

Female clients and partners/vendors/sponsors that we work with in the triathlon industry

Industry/Entity Type

Fitness

Contact Information for Business Card

Pace with Us Fitness (business name)
Nina Carver
Business Director
Mobile: 0438 916 207
Email: nina@pacewithusfitness.com.au
www.pacewithusfitness.com.au

Second business card:
Pace with Us Fitness
Bel Stray
Coaching Director
Mobile: 0459 260 718
Email: bel@pacewithusfitness.com.au

Font styles to use
Serif
Sans Serif

Requirements
Must have
• Core contact details above, our logo and be a printable design
Should not have
• Pink
• Cursive/script fonts

```html
<!DOCTYPE html>
<html lang="en">
<head>
<meta charset="utf-8">
<title>Pace with Us Fitness — Business Card</title>
<link rel="stylesheet" href="https://fonts.googleapis.com/css2?family=Open+Sans:wght@400;600;700&display=swap">
<style>
  :root {
    --backdrop: #e7e5e1;
    --card-black: #000000;
    --teal: #1ec8d8;
    --grey: #8f9296;
    --text-light: #e6e8ea;
    --band-deep: #0b2a8c;
    --band-mid: #1a4ccf;
    --band-light: #2f6ee6;
  }
  * { margin: 0; padding: 0; box-sizing: border-box; }
  html, body {
    width: 1200px;
    height: 900px;
    overflow: hidden;
    background: var(--backdrop);
    font-family: "Open Sans", Arial, sans-serif;
  }
  .canvas {
    width: 1200px;
    height: 900px;
    display: flex;
    align-items: center;
    justify-content: center;
  }
  .business-card {
    position: relative;
    width: 900px;
    height: 540px;
    background: var(--card-black);
    overflow: hidden;
    box-shadow: 0 10px 30px rgba(0,0,0,0.25);
  }
  .brand {
    position: absolute;
    left: 64px;
    top: 196px;
    display: flex;
    align-items: center;
    gap: 16px;
  }
  .brand-square {
    width: 30px;
    height: 30px;
    background: var(--teal);
  }
  .brand-name {
    color: var(--teal);
    font-weight: 700;
    font-size: 34px;
    letter-spacing: 1px;
    text-transform: uppercase;
  }
  .contact {
    position: absolute;
    right: 44px;
    top: 44px;
    text-align: right;
  }
  .contact-name {
    color: var(--teal);
    font-weight: 700;
    font-size: 26px;
    letter-spacing: 1px;
    text-transform: uppercase;
    line-height: 1.1;
  }
  .contact-title {
    color: var(--grey);
    font-size: 17px;
    margin-top: 4px;
    margin-right: 4px;
  }
  .contact-lines {
    margin-top: 44px;
    list-style: none;
  }
  .contact-line {
    display: flex;
    justify-content: flex-end;
    align-items: center;
    gap: 12px;
    color: var(--text-light);
    font-size: 19px;
    letter-spacing: 0.6px;
    line-height: 30px;
  }
  .contact-icon {
    width: 18px;
    height: 18px;
    flex: none;
  }
  .contact-icon.blank { visibility: hidden; }
  .action-band {
    position: absolute;
    left: 0;
    bottom: 0;
    width: 100%;
    height: 215px;
    background:
      radial-gradient(ellipse at 55% 45%, var(--band-light) 0%, transparent 65%),
      linear-gradient(180deg, var(--band-mid) 0%, var(--band-deep) 100%);
  }
</style>
</head>
<body>
<main class="canvas">
  <article class="business-card">
    <div class="brand">
      <span class="brand-square"></span>
      <span class="brand-name">Pace with Us Fitness</span>
    </div>

    <section class="contact">
      <h1 class="contact-name">Nina Carver</h1>
      <p class="contact-title">Business Director</p>
      <ul class="contact-lines">
        <li class="contact-line">0438 916 207
          <svg class="contact-icon" viewBox="0 0 18 18" aria-hidden="true">
            <rect x="5" y="1.5" width="8" height="15" rx="1.5" fill="none" stroke="var(--teal)" stroke-width="1.6"/>
            <line x1="8" y1="14" x2="10" y2="14" stroke="var(--teal)" stroke-width="1.4"/>
          </svg>
        </li>
        <li class="contact-line">nina@pacewithusfitness.com.au
          <svg class="contact-icon" viewBox="0 0 18 18" aria-hidden="true">
            <rect x="1.5" y="4" width="15" height="10" fill="none" stroke="var(--teal)" stroke-width="1.6"/>
            <polyline points="1.5,4 9,10 16.5,4" fill="none" stroke="var(--teal)" stroke-width="1.6"/>
          </svg>
        </li>
        <li class="contact-line">www.pacewithusfitness.com.au
          <svg class="contact-icon" viewBox="0 0 18 18" aria-hidden="true">
            <rect x="1.5" y="2.5" width="15" height="10" fill="none" stroke="var(--teal)" stroke-width="1.6"/>
            <line x1="9" y1="12.5" x2="9" y2="15.5" stroke="var(--teal)" stroke-width="1.6"/>
            <line x1="5.5" y1="15.5" x2="12.5" y2="15.5" stroke="var(--teal)" stroke-width="1.6"/>
          </svg>
        </li>
      </ul>
    </section>

    <div class="action-band" role="img" aria-label="Photo sequence of triathletes moving from swim, to bike ride, to run, on a blue background"></div>
  </article>
</main>
</body>
</html>
```